Retirement maintenance and reinstatment brochure

We are looking for a capability statement/brochure outlining our skills and capabilities for maintenance, reinstatement and refurbishment work specific to the requirements of retirement villages in Australia

We are a new company, however our people have significant experience working in this industry

Target Market(s)

Retirement living facilities, aged care facilities, hospitals

Industry/Entity Type

Building

Colors

Designer to choose colors to be used in the design.

Requirements
Must have
• Not alot of wording. Stock images of building refurbishment to retirement living and aged care (carpenters, painters etc)
Nice to have
• 1-2 pages only
Should not have
• alot of meaningless writing

```html
<!DOCTYPE html>
<html lang="en">
<head>
<meta charset="utf-8">
<title>Keystone Care Maintenance Solutions – Brochure</title>
<link href="https://fonts.googleapis.com/css2?family=Teko:wght@500;600&family=Open+Sans:wght@400;600;700&display=swap" rel="stylesheet">
<style>
  :root{
    --red:#d3202f;
    --blue:#1d63ad;
    --blue-dark:#174a86;
    --blue-mid:#2a74c4;
    --ink:#2b2b2b;
    --paper:#ffffff;
    --bg:#e9eaec;
    --pink:#f3d9d6;
  }
  *{box-sizing:border-box;margin:0;padding:0}
  html,body{width:845px;height:1200px;overflow:hidden;background:var(--bg)}
  body{position:relative;font-family:"Open Sans",Arial,sans-serif;color:var(--ink)}
  .spread{position:absolute;left:20px;width:805px;height:570px;background:var(--paper);overflow:hidden;box-shadow:0 2px 8px rgba(0,0,0,.15)}
  .spread--outside{top:20px}
  .spread--inside{top:610px}
  .spread__art{position:absolute;inset:0;width:805px;height:570px}
  .fold{position:absolute;top:0;left:392px;width:20px;height:570px;background:linear-gradient(90deg,rgba(0,0,0,0),rgba(0,0,0,.08),rgba(0,0,0,0))}
  .heading{font-family:"Teko",sans-serif;font-weight:600;color:var(--red);line-height:1;letter-spacing:.5px;text-transform:uppercase}
  .about__title{position:absolute;left:38px;top:34px;font-size:50px}
  .about__text{position:absolute;left:40px;top:88px;width:190px;font-size:11px;line-height:1.45}
  .photo{position:absolute}
  .photo--plaster{left:40px;top:180px;width:150px;height:150px;border-radius:50%;border:5px solid var(--red);background:radial-gradient(circle at 60% 40%,#f2f2f2,#c9ccd0)}
  .pink-block{position:absolute;background:var(--pink);opacity:.7}
  .photo--painter{left:95px;top:270px;width:160px;height:300px;background:linear-gradient(180deg,#cfc7c2,#8c6f66 45%,#e6e3df)}
  .brand{display:flex;align-items:center;gap:6px}
  .brand__dot{width:20px;height:20px;border-radius:50%;background:var(--blue);flex:none}
  .brand__name{font-family:"Open Sans",sans-serif;font-weight:700;color:var(--blue);font-size:12px;line-height:1.1;text-transform:uppercase;white-space:nowrap}
  .brand__name small{display:block;font-size:6.5px;letter-spacing:.8px}
  .contact{position:absolute;left:264px;top:400px;width:128px}
  .contact__title{margin-top:10px;font-size:11px;font-weight:700;color:var(--blue);line-height:1.25}
  .contact__title span{display:block;font-weight:400}
  .contact__list{list-style:none;margin-top:6px;font-size:9px;line-height:1.45}
  .contact__list li{display:flex;align-items:flex-start;gap:5px}
  .contact__list svg{width:9px;height:9px;flex:none;margin-top:3px}
  .brand--cover{position:absolute;left:590px;top:420px}
  .brand--cover .brand__dot{width:34px;height:34px}
  .brand--cover .brand__name{font-size:20px}
  .brand--cover .brand__name small{font-size:8.5px;letter-spacing:1px}
  .profile__title{position:absolute;left:30px;top:222px;font-size:52px}
  .profile__text{position:absolute;left:30px;top:278px;width:355px;font-size:11px;line-height:1.5}
  .feature{position:absolute;top:400px;height:170px;color:#fff;text-align:center;padding:18px 18px 0}
  .feature--ability{left:0;width:195px;background:var(--blue-dark)}
  .feature--licensed{left:195px;width:207px;background:var(--blue-mid)}
  .feature svg{width:34px;height:34px;display:block;margin:0 auto 8px}
  .feature__title{font-family:"Teko",sans-serif;font-weight:600;font-size:20px;text-transform:uppercase;line-height:1}
  .feature__text{margin-top:8px;font-size:10px;line-height:1.45}
  .trades__title{position:absolute;left:425px;top:26px;font-size:36px}
  .trade{position:absolute;width:135px;text-align:center}
  .trade__photo{height:58px;border:2px solid #fff;box-shadow:0 1px 4px rgba(0,0,0,.25)}
  .trade__label{margin-top:4px;font-size:9.5px;font-weight:600;line-height:1.2}
</style>
</head>
<body>

<section class="spread spread--outside">
  <svg class="spread__art" viewBox="0 0 805 570">
    <defs>
      <clipPath id="page-clip"><rect width="805" height="570"/></clipPath>
      <linearGradient id="swoosh" x1="0" y1="0" x2="1" y2="0">
        <stop offset="0" stop-color="#1b4f92"/><stop offset="1" stop-color="#2f7fd0"/>
      </linearGradient>
      <linearGradient id="workshop" x1="0" y1="0" x2="1" y2="1">
        <stop offset="0" stop-color="#d9b48a"/><stop offset=".5" stop-color="#8a5a3c"/><stop offset="1" stop-color="#c49a78"/>
      </linearGradient>
    </defs>
    <g clip-path="url(#page-clip)">
      <circle cx="520" cy="110" r="205" fill="url(#workshop)" role="img" aria-label="Carpenter measuring timber at a workbench"/>
      <path d="M304 235 A250 250 0 0 0 736 235" fill="none" stroke="var(--red)" stroke-width="6"/>
      <path d="M298 149 A225 225 0 0 0 731 187" fill="none" stroke="url(#swoosh)" stroke-width="42"/>
      <polygon points="773,202 689,172 748,140" fill="#2f7fd0"/>
    </g>
  </svg>
  <div class="fold"></div>

  <h2 class="heading about__title">About</h2>
  <p class="about__text">Keystone Care Maintenance Solutions is a commercial building and maintenance company established and located on the Sunshine Coast in QLD.</p>

  <div class="pink-block" style="left:60px;top:330px;width:90px;height:90px"></div>
  <div class="pink-block" style="left:230px;top:300px;width:70px;height:70px"></div>
  <div class="photo photo--painter" role="img" aria-label="Smiling painter in overalls holding a paint roller"></div>
  <div class="photo photo--plaster" role="img" aria-label="Hand smoothing plaster on a wall with a trowel"></div>

  <div class="contact">
    <div class="brand">
      <span class="brand__dot"></span>
      <span class="brand__name">Keystone Care<small>Maintenance Solutions</small></span>
    </div>
    <p class="contact__title">KEYSTONE CARE<span>Maintenance Solutions</span></p>
    <ul class="contact__list">
      <li><svg viewBox="0 0 10 10"><path d="M5 0a3.5 3.5 0 0 0-3.5 3.5C1.5 6 5 10 5 10s3.5-4 3.5-6.5A3.5 3.5 0 0 0 5 0zm0 5a1.5 1.5 0 1 1 0-3 1.5 1.5 0 0 1 0 3z" fill="var(--red)"/></svg>Lorem Ipsum is simply dummy text of the printing</li>
      <li><svg viewBox="0 0 10 10"><path d="M2 0l2 2.5-1 1.2a6 6 0 0 0 3.3 3.3l1.2-1L10 8l-1.3 1.6C5 10 0 5 .4 1.3z" fill="var(--red)"/></svg>(000) 000-0000</li>
      <li><svg viewBox="0 0 10 10"><path d="M2 0l2 2.5-1 1.2a6 6 0 0 0 3.3 3.3l1.2-1L10 8l-1.3 1.6C5 10 0 5 .4 1.3z" fill="var(--red)"/></svg>(000) 000-000</li>
    </ul>
  </div>

  <div class="brand brand--cover">
    <span class="brand__dot"></span>
    <span class="brand__name">Keystone Care<small>Maintenance Solutions</small></span>
  </div>
</section>

<section class="spread spread--inside">
  <svg class="spread__art" viewBox="0 0 805 570">
    <defs>
      <clipPath id="inside-clip"><rect width="805" height="570"/></clipPath>
      <linearGradient id="facade" x1="0" y1="0" x2="1" y2="0">
        <stop offset="0" stop-color="#e6e2d8"/><stop offset=".55" stop-color="#cfc6b4"/><stop offset=".6" stop-color="#b49a6e"/><stop offset="1" stop-color="#8f8778"/>
      </linearGradient>
      <linearGradient id="tools" x1="0" y1="0" x2="1" y2="1">
        <stop offset="0" stop-color="#e8d3b0"/><stop offset="1" stop-color="#a9794a"/>
      </linearGradient>
    </defs>
    <rect x="0" y="0" width="402" height="240" fill="url(#facade)" role="img" aria-label="Facade of an old building with tall windows under refurbishment"/>
    <path d="M0 215 Q200 172 402 200 L402 570 L0 570 Z" fill="var(--paper)"/>
    <g clip-path="url(#inside-clip)">
      <circle cx="700" cy="540" r="125" fill="url(#tools)" role="img" aria-label="Woodworking chisels laid on a timber bench"/>
      <path d="M700 400 A140 140 0 0 1 838 516" fill="none" stroke="var(--red)" stroke-width="14"/>
      <path d="M700 400 A140 140 0 0 0 562 516" fill="none" stroke="var(--blue)" stroke-width="22"/>
      <polygon points="533,511 591,521 553,561" fill="var(--blue)"/>
    </g>
  </svg>
  <div class="fold"></div>

  <h2 class="heading profile__title">Profile</h2>
  <p class="profile__text">We have expertise in retirement living and aged care maintenance works such as cleaning and painting programs, reinstatement works including painting and carpet replacement as well as major refurbishment or upgrade works including kitchen and bathroom works, electrical and air conditioning upgrade works.</p>

  <div class="feature feature--ability">
    <svg viewBox="0 0 34 34" fill="none" stroke="#e0606b" stroke-width="1.6"><circle cx="17" cy="13" r="4"/><path d="M10 26c1-5 4-7 7-7s6 2 7 7"/><circle cx="17" cy="3" r="2"/><circle cx="4" cy="12" r="2"/><circle cx="30" cy="12" r="2"/><circle cx="6" cy="28" r="2"/><circle cx="28" cy="28" r="2"/></svg>
    <h3 class="feature__title">Ability</h3>
    <p class="feature__text">We have the ability to react quickly and complete works with as little as 24 hours notice.</p>
  </div>
  <div class="feature feature--licensed">
    <svg viewBox="0 0 34 34" fill="none" stroke="#fff" stroke-width="1.6"><rect x="7" y="3" width="18" height="24" rx="1"/><path d="M11 9h10M11 13h10M11 17h6"/><circle cx="24" cy="25" r="4" fill="var(--red)" stroke="var(--red)"/></svg>
    <h3 class="feature__title">Licensed &amp; Insured</h3>
    <p class="feature__text">We are licensed and insured, and have a full workplace health and safety compliance system.</p>
  </div>

  <h2 class="heading trades__title">Trades we specialise in:</h2>

  <div class="trade" style="left:440px;top:80px"><div class="trade__photo" role="img" aria-label="Worker cleaning a building exterior" style="background:linear-gradient(135deg,#d7e6ef,#6b9a8f)"></div><p class="trade__label">Painting and building cleaning</p></div>
  <div class="trade" style="left:440px;top:170px"><div class="trade__photo" role="img" aria-label="Plasterer rendering an interior wall" style="background:linear-gradient(135deg,#eef0f2,#9aa7b8)"></div><p class="trade__label">Plastering and rendering</p></div>
  <div class="trade" style="left:440px;top:260px"><div class="trade__photo" role="img" aria-label="Electrician in hard hat at a switchboard" style="background:linear-gradient(135deg,#3f6fa8,#e0b64a)"></div><p class="trade__label">Electrical</p></div>
  <div class="trade" style="left:440px;top:350px"><div class="trade__photo" role="img" aria-label="Technician servicing an outdoor air conditioning unit" style="background:linear-gradient(135deg,#b9c1c8,#4d6e9a)"></div><p class="trade__label">Air conditioning upgrades</p></div>
  <div class="trade" style="left:645px;top:120px"><div class="trade__photo" role="img" aria-label="Power drill and hand tools" style="background:linear-gradient(135deg,#e9e7e2,#b59a55)"></div><p class="trade__label">Carpentry and minor repairs</p></div>
  <div class="trade" style="left:645px;top:215px"><div class="trade__photo" role="img" aria-label="Measuring tape on timber floor boards" style="background:linear-gradient(135deg,#e8cfa8,#b07f4f)"></div><p class="trade__label">Carpet and floor laying</p></div>
  <div class="trade" style="left:645px;top:310px"><div class="trade__photo" role="img" aria-label="Plumber fitting pipes under a sink" style="background:linear-gradient(135deg,#d6dde3,#5e7f9e)"></div><p class="trade__label">Plumbing</p></div>
</section>

</body>
</html>
```